K&T Fixit and Rebuild general contracting business card design

I already have a logo that I want to use and I need a card that uses that logo and color scheme on the front with the address phone numbers and email and on the back a place for technicians to write in their name and phone number when they hand it out. It will need the License number of License #KTFXTRB318QN.
It should say General Contractor under the company name. The address is
4417 NE 3rd Ave, Ste D246
Vancouver, WA 98612
www.kandtfixitandrebuild.example
office@kandtfixitandrebuild.example
360-555-0182 is the telephone number
360-555-0149 is the fax number

Target Market(s)

Homeowners needing remodel work or repairs in their home.

Industry/Entity Type

Construction

Contact Information for Business Card

Business name, address, phone number, license number, fax number, email, and website on the front and a place to fill in technician's name and number

Font styles to use
Serif

Requirements
Must have
• Business name, address, phone number, license number, fax number, email, and website on the front and a place to fill in technician's name and number
Nice to have
• I uploaded an example of a front that is good.
Should not have
• Froo froo or extra embellishments.

```html
<!DOCTYPE html>
<html lang="en">
<head>
<meta charset="utf-8">
<title>K&amp;T Fixit and Rebuild – Business Card</title>
<link href="https://fonts.googleapis.com/css2?family=Noto+Serif:wght@400;600&display=swap" rel="stylesheet">
<style>
  :root {
    --copper: #b0643a;
    --ink: #5a5a5a;
    --rule: #8a8a8a;
    --card: #ffffff;
    --backdrop: #d9d9d9;
    --backdrop-dark: #c4c4c4;
  }
  * { box-sizing: border-box; margin: 0; padding: 0; }
  html, body { width: 1200px; height: 801px; overflow: hidden; }
  body {
    background: radial-gradient(ellipse at 40% 35%, var(--backdrop) 0%, var(--backdrop-dark) 100%);
    font-family: "Noto Serif", serif;
    position: relative;
  }
  .card {
    position: absolute;
    top: 246px;
    width: 540px; height: 309px;
    background: var(--card);
    border-bottom: 3px solid var(--copper);
    box-shadow: 0 8px 22px rgba(0,0,0,.18);
  }
  .card--front { left: 45px; }
  .card--back { left: 615px; }

  /* brand block */
  .brand {
    position: absolute; left: 24px; top: 0; bottom: 0; width: 200px;
    display: flex; align-items: center; gap: 10px;
  }
  .brand__mark { width: 14px; height: 14px; background: var(--copper); flex: none; }
  .brand__name {
    display: block;
    color: var(--copper); font-weight: 600; font-size: 23px; line-height: 1.2;
  }
  .brand__tagline {
    display: block; margin-top: 6px;
    color: var(--ink); font-weight: 400; font-size: 12px;
    letter-spacing: .12em; text-transform: uppercase;
  }

  /* front */
  .divider {
    position: absolute; left: 232px; top: 70px; height: 170px;
    border-left: 1px solid var(--copper);
  }
  .contact {
    position: absolute; left: 248px; top: 66px;
    list-style: none; color: var(--ink); font-size: 13px; line-height: 23px;
  }
  .contact__license { color: var(--copper); }
  .contact__item { display: flex; align-items: center; gap: 7px; }
  .contact__item svg { width: 11px; height: 11px; fill: var(--copper); flex: none; }

  /* back */
  .card--back .brand {
    left: 0; right: 0; width: auto; top: 40px; bottom: auto;
    justify-content: center;
  }
  .card--back .brand__name { font-size: 28px; }
  .card--back .brand__tagline { text-align: center; font-size: 13px; }
  .fill-in {
    position: absolute; left: 40px; right: 40px; top: 150px;
    color: var(--copper); font-size: 15px;
  }
  .fill-in__row { display: flex; align-items: flex-end; gap: 6px; height: 38px; }
  .fill-in__line { flex: 1; border-bottom: 1px solid var(--rule); height: 1px; margin-bottom: 5px; }
</style>
</head>
<body>

<section class="card card--front" aria-label="Card front">
  <div class="brand">
    <span class="brand__mark"></span>
    <div>
      <span class="brand__name">K&amp;T Fixit<br>and Rebuild</span>
      <span class="brand__tagline">General Contractor</span>
    </div>
  </div>
  <div class="divider"></div>
  <ul class="contact">
    <li>4417 NE 3rd Ave, Ste D246</li>
    <li>Vancouver, WA 98612</li>
    <li class="contact__license">License #KTFXTRB318QN</li>
    <li class="contact__item">
      <svg viewBox="0 0 12 12" aria-hidden="true"><path d="M2.5 1l2 2.2-1 1.3c.7 1.5 1.8 2.6 3.3 3.3l1.3-1 2.2 2-1.3 1.7C5.2 10.2 1.8 6.8 1 2.3z"/></svg>
      360-555-0182</li>
    <li class="contact__item">
      <svg viewBox="0 0 12 12" aria-hidden="true"><rect x="3" y="1" width="6" height="3"/><rect x="1" y="4.5" width="10" height="4.5" rx="1"/><rect x="3" y="8" width="6" height="3"/></svg>
      360-555-0149</li>
    <li class="contact__item">
      <svg viewBox="0 0 12 12" aria-hidden="true"><path d="M1 2.5h10v7H1z M1 2.5l5 4 5-4" stroke="#fff" stroke-width=".8"/></svg>
      office@kandtfixitandrebuild.example</li>
    <li class="contact__item">
      <svg viewBox="0 0 12 12" aria-hidden="true"><circle cx="6" cy="6" r="5"/></svg>
      www.kandtfixitandrebuild.example</li>
  </ul>
</section>

<section class="card card--back" aria-label="Card back">
  <div class="brand">
    <span class="brand__mark"></span>
    <div>
      <span class="brand__name">K&amp;T Fixit and Rebuild</span>
      <span class="brand__tagline">General Contractor</span>
    </div>
  </div>
  <div class="fill-in">
    <div class="fill-in__row"><span class="fill-in__line"></span></div>
    <div class="fill-in__row"><span>Name:</span><span class="fill-in__line"></span></div>
    <div class="fill-in__row"><span>Contact:</span><span class="fill-in__line"></span></div>
  </div>
</section>

</body>
</html>
```